Esthetically Pleasing Core Values and Brand Promise for Accounting Firm

I would like a cohesive design that ties together my core values and brand promise. My firm, Maple Finch Advisory, provides accounting work to small businesses. I prefer modern and clean designs. I want my Core Values and Brand Promise to represent me - sole entrepreneur, married, mother of two kids, modern esthetics, clean lines, organized, colorful (teals, greys, white, yellows)

Industry/Entity Type

Public Accounting

Colors
33b8a4

```html
<!DOCTYPE html>
<html lang="en">
<head>
<meta charset="utf-8">
<title>Maple Finch Advisory – Core Values</title>
<link rel="stylesheet" href="https://fonts.googleapis.com/css2?family=Questrial&family=Montserrat:wght@600;700&family=Lato:wght@400;700&display=swap">
<style>
  :root {
    --teal: #33b8a4;
    --teal-deep: #1f8f86;
    --lime: #dde323;
    --charcoal: #3c3c3c;
    --charcoal-light: #595959;
    --ink: #3a3a3a;
    --white: #ffffff;
    --backdrop: #ebe8e4;
  }
  * { box-sizing: border-box; margin: 0; padding: 0; }
  html, body {
    width: 1200px; height: 1200px; overflow: hidden;
    background: var(--backdrop);
  }
  .flyer {
    position: absolute; left: 158px; top: 33px;
    width: 884px; height: 1134px;
    background: var(--white);
    overflow: hidden;
  }
  .brand-name {
    position: absolute; left: 40px; top: 52px; width: 392px;
    text-align: center; color: var(--teal-deep);
    font-family: "Questrial", sans-serif; font-weight: 400;
    line-height: 1;
  }
  .brand-name .line-lg { display: block; font-size: 66px; letter-spacing: 4px; }
  .brand-name .line-sm { display: block; font-size: 28px; letter-spacing: 5px; margin-top: 8px; }
  .title-block {
    position: absolute; left: 40px; top: 257px; width: 412px; height: 193px;
    background: var(--teal);
    color: var(--white);
    font-family: "Questrial", sans-serif;
    font-size: 90px; line-height: 0.98; letter-spacing: -1px;
    padding: 12px 0 0 24px;
  }
  .photo {
    position: absolute; left: 452px; top: 0; width: 432px; height: 547px;
    background: linear-gradient(160deg, #8fa3b8 0%, #c9d2da 40%, #e6e8ea 70%, #b9bfc4 100%);
  }
  .values-panel {
    position: absolute; left: 0; top: 468px; width: 452px; height: 639px;
    background: linear-gradient(135deg, var(--charcoal) 0%, var(--charcoal-light) 55%, var(--charcoal) 100%);
  }
  .item { position: absolute; }
  .item .badge {
    position: absolute; left: 0; top: 0; width: 76px; height: 76px;
    border-radius: 50%; background: var(--lime);
    display: flex; align-items: center; justify-content: center;
  }
  .item .badge svg { width: 42px; height: 42px; }
  .item h3 {
    position: absolute; left: 105px; top: 2px; white-space: nowrap;
    font-family: "Montserrat", sans-serif; font-weight: 700;
    font-size: 20px; letter-spacing: 2px;
  }
  .item p {
    position: absolute; left: 105px; top: 36px; width: 275px;
    font-family: "Lato", sans-serif; font-size: 15.5px; line-height: 1.38;
  }
  .values-panel .item h3 { color: var(--lime); }
  .values-panel .item p { color: var(--white); }
  .promise {
    position: absolute; left: 472px; top: 567px; width: 412px; height: 119px;
    background: var(--charcoal);
    color: var(--lime);
    font-family: "Montserrat", sans-serif; font-weight: 700;
    font-size: 20px; letter-spacing: 2px; line-height: 1.35;
    padding: 22px 16px;
  }
  .services .item h3 { color: var(--ink); font-family: "Montserrat", sans-serif; font-weight: 600; }
  .services .item p { color: var(--ink); width: 270px; }
  .foot-band {
    position: absolute; left: 0; top: 1111px; width: 884px; height: 23px;
    background: var(--teal);
  }
</style>
</head>
<body>
<main class="flyer">
  <div class="brand-name">
    <span class="line-lg">MAPLE</span>
    <span class="line-lg">FINCH</span>
    <span class="line-sm">ADVISORY</span>
  </div>

  <h1 class="title-block">CORE<br>VALUES</h1>

  <div class="photo" role="img" aria-label="Photo of two businesspeople shaking hands over a desk with a calculator, financial charts and a tablet"></div>

  <section class="values-panel">
    <div class="item" style="left:57px; top:34px;">
      <div class="badge">
        <svg viewBox="0 0 42 42" fill="none" stroke="#3c3c3c" stroke-width="2.6" stroke-linejoin="round">
          <rect x="11" y="9" width="20" height="12" rx="3"/>
          <path d="M17 9v12M24 9v12M11 21v7a6 6 0 0 0 6 6h7a7 7 0 0 0 7-7v-6"/>
        </svg>
      </div>
      <h3>EMPOWER</h3>
      <p>we are dedicated, appreciative and respectful of people's time and purpose.</p>
    </div>
    <div class="item" style="left:57px; top:193px;">
      <div class="badge">
        <svg viewBox="0 0 42 42" fill="none" stroke="#3c3c3c" stroke-width="2.4">
          <circle cx="21" cy="21" r="11"/>
          <circle cx="21" cy="18" r="4"/>
          <path d="M14 28a8 8 0 0 1 14 0"/>
          <path d="M4 12V4h8M30 4h8v8M38 30v8h-8M12 38H4v-8"/>
        </svg>
      </div>
      <h3>CLIENT FOCUSED</h3>
      <p>we provide a personal service that goes above the standards of professional care.</p>
    </div>
    <div class="item" style="left:57px; top:347px;">
      <div class="badge">
        <svg viewBox="0 0 42 42" fill="none" stroke="#3c3c3c" stroke-width="2.4" stroke-linejoin="round">
          <path d="M21 5v30M8 10h26M13 37h16"/>
          <path d="M8 10l-5 12h10zM34 10l-5 12h10z"/>
        </svg>
      </div>
      <h3>RECTITUDE</h3>
      <p>we know the difference between what we have the right to do and what the right thing to do is.</p>
    </div>
    <div class="item" style="left:57px; top:501px;">
      <div class="badge">
        <svg viewBox="0 0 42 42" fill="#3c3c3c">
          <rect x="5" y="19" width="7" height="16" rx="1"/>
          <path d="M14 19l7-12c2-2 5 0 4 3l-2 7h11c2 0 4 2 3 4l-3 12c-1 2-2 2-4 2H14z"/>
        </svg>
      </div>
      <h3>RELENTLESS</h3>
      <p>we believe that the longer we try to do our best, the better we become.</p>
    </div>
  </section>

  <h2 class="promise">BRAND PROMISE –<br>TRUST, TRANSPARENCY AND DEPENDABILITY</h2>

  <section class="services">
    <div class="item" style="left:494px; top:732px;">
      <div class="badge">
        <svg viewBox="0 0 42 42" fill="none" stroke="#3c3c3c" stroke-width="2.2">
          <circle cx="21" cy="21" r="12"/>
          <path d="M21 3v6M21 33v6M3 21h6M33 21h6M8 8l4 4M30 30l4 4M34 8l-4 4M12 30l-4 4"/>
          <text x="21" y="24.5" text-anchor="middle" font-family="Lato, sans-serif" font-size="9" font-weight="700" fill="#3c3c3c" stroke="none">TAX</text>
        </svg>
      </div>
      <h3>TAX</h3>
      <p>Maple Finch provides all clients with a trusted tax advisor who provides accuracy in all filings and ensures your compliance with all government agencies.</p>
    </div>
    <div class="item" style="left:494px; top:938px;">
      <div class="badge">
        <svg viewBox="0 0 42 42" fill="none" stroke="#3c3c3c" stroke-width="2.4" stroke-linejoin="round">
          <rect x="11" y="5" width="20" height="32" rx="2"/>
          <rect x="15" y="10" width="12" height="6"/>
          <path d="M15 22h2M20 22h2M25 22h2M15 27h2M20 27h2M25 27h2M15 32h2M20 32h2M25 32h2"/>
        </svg>
      </div>
      <h3>ACCOUNTING</h3>
      <p>Maple Finch provides all business owners with the financial visibility needed to foster growth and facilitate goals.</p>
    </div>
  </section>

  <div class="foot-band"></div>
</main>
</body>
</html>
```